M25 Billboard Advert Required Please

I need an advert for a motorway Billboard on the M25 , the advert should show the following in big letters:
GUTTER CLEANING
DALRYNFLUES.COM and a small logo off to the side (Our logo is attached)

The printer has requested the following (Important please) the advert has to be
pdf file / 300 dpi/landscape orientation / scaled to a minimum 25% advert size ( this particular site is 22ft x 10ft so 25% of this please). Please also make sure that the artwork is embedded and outlined correctly if this is incorrect it will affect the printing of the banner.

Target Market(s)

General Public

Industry/Entity Type

Gutter Cleaning

Requirements
Should not have
• No Change to our Logo

```html
<!DOCTYPE html>
<html lang="en">
<head>
<meta charset="utf-8">
<title>Dalryn Flues – Gutter Cleaning Billboard</title>
<link href="https://fonts.googleapis.com/css2?family=Poppins:wght@600;700;800&family=Open+Sans:wght@600&display=swap" rel="stylesheet">
<style>
  :root {
    --page-bg: #e6e6e6;
    --paper: #ffffff;
    --ink: #0b0607;
    --brand-red: #b5081b;
    --photo-dark: #4a4f52;
    --photo-mid: #7d8285;
    --photo-roof: #2f5a58;
    --haze: #ececec;
  }
  * { margin: 0; padding: 0; box-sizing: border-box; }
  html, body { width: 856px; height: 1200px; overflow: hidden; }
  body { background: var(--page-bg); position: relative; }

  .billboard {
    position: absolute;
    left: 62px; top: 434px;
    width: 733px; height: 332px;
    background: var(--paper);
    box-shadow: 6px 8px 14px rgba(0,0,0,0.35);
    overflow: hidden;
  }
  .billboard-shapes { position: absolute; inset: 0; }

  .brand {
    position: absolute; left: 40px; top: 26px;
    display: flex; align-items: center; gap: 10px;
  }
  .brand-mark { width: 14px; height: 14px; background: var(--brand-red); }
  .brand-name {
    font-family: 'Poppins', sans-serif; font-weight: 700;
    font-size: 28px; line-height: 1; color: var(--ink); letter-spacing: -0.5px;
  }
  .tagline {
    position: absolute; left: 40px; top: 74px;
    font-family: 'Open Sans', sans-serif; font-weight: 600;
    font-size: 11.5px; color: var(--ink);
  }

  .headline { position: absolute; left: 32px; top: 96px; font-family: 'Poppins', sans-serif; font-weight: 800; line-height: 0.9; }
  .headline-top { display: block; font-size: 80px; color: var(--ink); letter-spacing: -1px; }
  .headline-bottom { display: block; font-size: 61px; color: var(--brand-red); letter-spacing: 0.5px; }

  .phone {
    position: absolute; left: 38px; top: 272px;
    display: flex; align-items: center; gap: 4px;
    font-family: 'Poppins', sans-serif; font-weight: 600;
    font-size: 30px; line-height: 1; color: var(--paper);
  }
  .phone-icon { width: 24px; height: 24px; }

  .web-address {
    position: absolute; left: 375px; top: 286px;
    font-family: 'Poppins', sans-serif; font-weight: 700;
    font-size: 19px; line-height: 1; color: var(--paper);
    letter-spacing: 4.4px;
  }
</style>
</head>
<body>
  <section class="billboard">
    <svg class="billboard-shapes" width="733" height="332" viewBox="0 0 733 332" aria-hidden="false">
      <defs>
        <linearGradient id="hazeFade" x1="0" x2="1" y1="0" y2="0">
          <stop offset="0" stop-color="#ffffff"/>
          <stop offset="1" stop-color="#e4e4e4"/>
        </linearGradient>
        <linearGradient id="photoTone" x1="0" x2="1" y1="0" y2="1">
          <stop offset="0" stop-color="#8a8f92"/>
          <stop offset="0.45" stop-color="#4a4f52"/>
          <stop offset="0.8" stop-color="#3b3a36"/>
          <stop offset="1" stop-color="#2f5a58"/>
        </linearGradient>
      </defs>
      <rect class="backdrop-haze" x="200" y="0" width="230" height="248" fill="url(#hazeFade)" role="img" aria-label="Faded photo of a worker on a tiled roof"/>
      <polygon class="hero-photo" points="430,0 733,0 733,256 330,256 345,224 420,224" fill="url(#photoTone)" role="img" aria-label="Photo of a kneeling worker in work boots and yellow gloves clearing leaves from a roof gutter"/>
      <polygon class="phone-band" points="0,248 377,248 340,332 0,332" fill="var(--ink)"/>
      <polygon class="web-band" points="371,263 733,263 733,332 340,332" fill="var(--brand-red)"/>
    </svg>

    <div class="brand">
      <span class="brand-mark"></span>
      <span class="brand-name">Dalryn Flues</span>
    </div>
    <p class="tagline">Clean gutters protect your property</p>

    <h1 class="headline">
      <span class="headline-top">GUTTER</span>
      <span class="headline-bottom">CLEANING</span>
    </h1>

    <div class="phone">
      <svg class="phone-icon" viewBox="0 0 24 24" aria-hidden="true">
        <path d="M6.6 3.5l3 3.4-1.8 2.3c1.2 2.6 3.1 4.6 5.8 5.9l2.3-1.8 3.4 3-1.6 3.2c-.4.7-1.2 1-2 .8C9.6 18.7 5.3 14.4 3.7 8.3c-.2-.8.1-1.6.8-2z" fill="var(--brand-red)"/>
        <path d="M14 3.5a6.5 6.5 0 0 1 6.5 6.5M14 6.5a3.5 3.5 0 0 1 3.5 3.5" stroke="var(--brand-red)" stroke-width="1.6" fill="none" stroke-linecap="round"/>
      </svg>
      <span class="phone-number">+44 800 555 0193</span>
    </div>

    <p class="web-address">WWW.DALRYNFLUES.COM</p>
  </section>
</body>
</html>
```